Corwin Ashby Foundation Flyer

Design a two sided flyer that will be used to solicit charitable donations from local residents and businesses for a new school gymnasium. The fundraising project is being done by the Corwin Ashby Foundation. I have attached two files for: 1. "Original" Flyer 2. "Revised" Copy. Please use "revised" for the copy. You can refer to "original" for illustrations and pictures. The Corwin Ashby Foundation does not have a logo, so you can create one. It should be simple and understated.

```html
<!DOCTYPE html>
<html lang="en">
<head>
<meta charset="utf-8">
<title>Corwin Ashby Foundation Flyer</title>
<link href="https://fonts.googleapis.com/css2?family=Arimo:ital,wght@0,400;0,700;1,400;1,700&display=swap" rel="stylesheet">
<style>
  :root{
    --blue:#0660b6;
    --ink:#4a4a4a;
    --panel:#eeeeee;
    --panel-line:#9a9a9a;
    --paper:#ffffff;
    --backdrop:#626262;
  }
  *{box-sizing:border-box;margin:0;padding:0}
  html,body{width:1200px;height:881px;overflow:hidden}
  body{background:var(--backdrop);font-family:"Arimo",Arial,sans-serif;color:var(--ink);position:relative}
  .page{position:absolute;top:100px;width:480px;height:679px;background:var(--paper)}
  .page--front{left:114px}
  .page--back{left:627px}

  .brand-band{position:absolute;left:0;top:10px;width:258px;height:80px;background:var(--blue);
    clip-path:polygon(0 0,233px 0,258px 80px,0 80px);display:flex;align-items:center;padding-left:29px}
  .brand-name{color:#fff;font-weight:400;font-size:17px;line-height:20px;letter-spacing:.5px}
  .project-title{position:absolute;right:22px;top:23px;text-align:right;font-weight:700;color:#555;font-size:18.5px;line-height:19px;letter-spacing:.6px}
  .project-title .light{font-weight:400;letter-spacing:0}

  .headline{position:absolute;left:27px;top:98px;color:var(--blue);font-weight:700;font-size:20.5px;line-height:23.5px}
  .salutation{position:absolute;left:25px;top:152px;color:var(--blue);font-weight:700;font-style:italic;font-size:10px}
  .intro{position:absolute;left:25px;top:166px;width:435px;font-style:italic;font-size:10px;line-height:11.7px}

  .panel{position:absolute;background:var(--panel);border:1px solid var(--panel-line);border-radius:4px;overflow:hidden}
  .page--front .panel{left:20px;top:219px;width:441px;height:439px;padding:9px 20px 0 19px}
  .page--back .panel{left:20px;top:24px;width:441px;height:496px;padding:17px 20px 0 17px}

  .section-head{position:relative;height:16px;border-bottom:1px solid var(--blue);margin-bottom:11px}
  .tab{position:absolute;left:0;bottom:-1px;height:16px;background:var(--blue);color:#fff;font-weight:700;font-style:italic;font-size:9.6px;line-height:16px;padding-left:4px;
    clip-path:polygon(0 0,calc(100% - 8px) 0,100% 100%,0 100%)}
  .copy{font-style:italic;font-size:9.8px;line-height:11.7px;text-align:justify;margin-bottom:11px}
  .copy + .copy{margin-top:-6px}
  .copy b{font-weight:700}
  .list{list-style:none;font-style:italic;font-size:9.8px;line-height:11.7px;margin-bottom:14px}
  .list li{position:relative;padding-left:14px}
  .list li::before{content:"•";position:absolute;left:0}
  .list--indent li{margin-left:14px}

  .contact{position:absolute;left:19px;top:527px;width:443px;height:134px;background:var(--blue);color:#fff;padding:10px 18px 0 24px}
  .contact-lead{font-weight:700;font-style:italic;font-size:15px;padding-bottom:4px;border-bottom:1px solid rgba(255,255,255,.7)}
  .contact-mid{display:flex;justify-content:space-between;align-items:center;padding:5px 0 4px;border-bottom:1px solid rgba(255,255,255,.7)}
  .person-name{font-weight:700;font-style:italic;font-size:19px;line-height:21px}
  .person-role{font-style:italic;font-size:12px;line-height:16px}
  .person-org{font-style:italic;font-size:11px;line-height:16px}
  .contact .brand-name{font-size:15px;line-height:17px}
  .contact-line{font-weight:700;font-style:italic;font-size:23px;line-height:30px;white-space:nowrap;margin-left:-4px}
</style>
</head>
<body>

<section class="page page--front">
  <div class="brand-band"><div class="brand-name">The<br>Corwin Ashby<br>Foundation</div></div>
  <div class="project-title">The Corwin Ashby<br>Memorial Gymnasium<br><span class="light">Project</span></div>

  <h1 class="headline">Lifting our community &amp; honoring<br>the life &amp; legacy of Corwin Ashby</h1>
  <p class="salutation">Dear Community Members, Friends and Supporters</p>
  <p class="intro">We invite you to join us in this journey of love and community that celebrates the life and legacy of a beloved local resident, Corwin Ashby. Corwin’s unwavering love for Halden Island and his profound belief in the power of community has inspired us to embark on this heartfelt initiative to build a new school gymnasium in his honor.</p>

  <div class="panel">
    <div class="section-head"><span class="tab" style="width:150px">Why Build a Gymnasium?</span></div>
    <p class="copy">One small community can come together in support of our Island youth. In July 2023, our community tragically lost Corwin Ashby in a horrific motorcycle accident. In tribute to Corwin’s remarkable spirit and love for the Halden Island school, the Corwin Ashby Foundation (a 501(c)(3) foundation) is seeking to lift our community and provide a much-needed facility for our community and students by building a much needed school gymnasium in Corwin’s honor.</p>
    <p class="copy">Currently, the school district doesn’t have an onsite gym. Students hold gym classes, practices, and scrimmages at a rented community gym which is a short walk from the school. The new gymnasium would benefit the students and community as well as serve as a living memorial to Corwin and other students who left us far too soon.<br>The new gym will be a place for our Island youth to have physical education classes as well as a place for our student-athletes to compete and host visiting teams.</p>
    <div class="section-head" style="margin-top:9px"><span class="tab" style="width:150px;padding-left:9px">The Vision</span></div>
    <p class="copy">The Corwin Ashby Memorial Gymnasium Concept will be an onsite facility that will be approximately 12,000 square feet and will cost $4.5 million. Attached directly to the school it will include a gymnasium with proper room for spectators, entry lobby, concession area, two team locker rooms and an equipment storage room.</p>
    <div class="section-head" style="margin-top:8px"><span class="tab" style="width:150px;padding-left:6px">Why Can’t the School Pay?</span></div>
    <p class="copy">The combination of revenue limits and sparse state aid has left many Wisconsin schools unable to meet their operational needs. Halden Island is one of the state's most severely underfunded school districts! This is NOT because they overspend but because they are severely underfunded. The school has no choice but to run on a bare-bones budget.</p>
    <div class="section-head" style="margin-top:-1px"><span class="tab" style="width:150px;padding-left:10px">How You Can Help</span></div>
    <p class="copy">To bring this vision to life, we need your help! We’re reaching out to ask for your generous donations to help fund the gym's construction. Your contribution will not only honor Corwin’s memory but will also create a lasting legacy that benefits our Island, our Students and our community.</p>
  </div>
</section>

<section class="page page--back">
  <div class="panel">
    <div class="section-head"><span class="tab" style="width:150px;padding-left:8px">Ways to Donate</span></div>
    <ul class="list" style="margin-top:5px">
      <li><b>Online:</b> GiveLink (address to come)</li>
      <li><b>In-Person:</b> Donations can be made at the front office of the Halden Island School, located at 412 Harbor Road.</li>
      <li><b>Mail:</b> Send checks payable to "Corwin Ashby Foundation" to P.O. Box 317, Halden Island, WI 54990</li>
    </ul>
    <div class="section-head"><span class="tab" style="width:150px;padding-left:8px">Sponsorship Opportunities</span></div>
    <p class="copy" style="margin-top:5px;margin-bottom:16px">We also offer sponsorship opportunities for individuals and businesses looking to make a significant impact. Sponsorships for various areas within the gymnasium and special recognition in our community events are available. For more information on sponsorships, please contact us at (555) 014-2290 or email info@corwinashbyfoundation.org.</p>
    <div class="section-head"><span class="tab" style="width:170px;padding-left:8px">Upcoming Fundraising Events</span></div>
    <p class="copy" style="margin-top:5px;margin-bottom:0">Join us for a series of events to raise funds and celebrate Corwin’s life:</p>
    <ul class="list list--indent"><li>Follow our Friendbook page for updates and events</li></ul>
    <div class="section-head"><span class="tab" style="width:115px;padding-left:8px">Stay Connected</span></div>
    <p class="copy" style="margin-top:5px;margin-bottom:0">Follow our progress and stay updated on upcoming events by visiting our website and following us on social media.</p>
    <ul class="list list--indent" style="margin-bottom:6px"><li>Friendbook: CorwinAshbyFoundation</li></ul>
    <div class="section-head"><span class="tab" style="width:213px;padding-left:8px">Together, Let’s Build Something Special</span></div>
    <p class="copy" style="margin-top:5px;margin-bottom:17px">Corwin Ashby’s legacy is one of vitality, inspiration, and Island Community Spirit. Let’s honor him by creating a place where his values continue to thrive and where everyone can feel good about our Island Community and meet the needs of our children and students. Your support is crucial to making this dream a reality.</p>
    <p class="copy" style="margin-bottom:11px">Thank you for your generosity and commitment to our community.</p>
    <p class="copy"><b>With heartfelt gratitude,</b><br>The Corwin Ashby Foundation</p>
  </div>

  <div class="contact">
    <div class="contact-lead">For more information, please reach out to</div>
    <div class="contact-mid">
      <div>
        <div class="person-name">Renata Ashby</div>
        <div class="person-role">President</div>
        <div class="person-org">Corwin Ashby Memorial Foundation</div>
      </div>
      <div class="brand-name">The<br>Corwin Ashby<br>Foundation</div>
    </div>
    <div class="contact-line">920-555-0147 | info@corwin|ashby</div>
  </div>
</section>

</body>
</html>
```